Launch of a new Investment fund

Im looking for someone design a logo and website for my Investment fund located in Singapore.

Attached to this project you will find a project scope document that details exactly what i am looking for and also includes a website copy that i have written up. I am happy for you to take your own inspiration as well to design the website. At this stage the website wont be very detailed as there isn't much information to showcase. I will require the website to be easily editable in the future so i can update it with progress the fund makes.

If you require any further details on the project please reach out to me

Coding

Coded - Design and coding required

Number of Pages Required

4 page

```html
<!DOCTYPE html>
<html lang="en">
<head>
<meta charset="utf-8">
<title>Kestrel Capital Management</title>
<link rel="stylesheet" href="https://fonts.googleapis.com/css2?family=Merriweather:wght@400;700&family=Lato:wght@400;700&display=swap">
<style>
:root{
  --ink:#161616;
  --white:#ffffff;
  --paper:#f2f2f2;
  --muted:#555555;
  --line:#e2e2e2;
  --sea-deep:#1f4f6e;
  --sea-light:#5c8aa6;
  --hull:#c9c4bd;
}
*{box-sizing:border-box;margin:0;padding:0}
html,body{width:1200px;height:3449px;overflow:hidden;background:var(--white);color:var(--ink);font-family:'Lato',sans-serif}
section,header,footer{position:relative;width:1200px}
.abs{position:absolute}

/* header */
.site-header{height:249px}
.brand{left:120px;top:26px;font-family:'Merriweather',serif;font-size:21px;line-height:25px;color:var(--ink)}
.main-nav{left:492px;top:44px;display:flex;gap:23px;font-size:16.5px}
.main-nav a,.footer-nav a{color:inherit;text-decoration:none}
.btn{background:var(--ink);color:var(--white);font-weight:700;display:flex;align-items:center;justify-content:center;font-size:17px}
.btn-start{left:960px;top:34px;width:127px;height:42px}
.hero-title{left:111px;top:118px;font-family:'Merriweather',serif;font-size:39px;line-height:49px;font-weight:400}

/* hero */
.hero{height:514px;background:linear-gradient(120deg,var(--sea-deep) 0%,var(--sea-light) 30%,var(--hull) 45%,#8a5a4f 60%,var(--sea-deep) 78%,#2f6686 100%)}
.btn-play{left:524px;top:229px;width:151px;height:56px;font-family:'Merriweather',serif;font-size:18px}

/* what we do */
.what{height:370px;background:var(--ink);color:var(--white)}
.what-title{left:112px;top:72px;font-family:'Merriweather',serif;font-size:42px;font-weight:700}
.what-copy{left:468px;top:62px;width:625px;font-size:15.2px;line-height:28.2px}

/* team */
.team{height:533px;background:var(--paper)}
.team-title{left:115px;top:84px;font-size:41px;font-family:'Merriweather',serif;font-weight:700}
.team-subtitle{left:115px;top:156px;font-size:24px;font-family:'Merriweather',serif;font-weight:400}
.team-copy{left:116px;top:228px;width:505px;font-size:15.2px;line-height:28.2px}
.portrait{left:765px;top:63px;width:322px;height:394px;background:linear-gradient(160deg,#8f979e 0%,#c6ccd1 45%,#2a3a5c 80%,#1c2740 100%)}

/* investments */
.invest{height:1019px}
.invest-title{left:115px;top:96px;font-size:41px;font-family:'Merriweather',serif;font-weight:700}
.invest-lead{left:115px;top:168px;width:950px;font-family:'Merriweather',serif;font-size:26px;line-height:41px}
.cards{left:111px;top:307px;display:flex}
.card{width:257px;height:367px;position:relative}
.card+.card{border-left:1px solid var(--line);padding-left:22px}
.card-title{margin-top:22px;font-family:'Merriweather',serif;font-weight:400;font-size:26px;line-height:33px;height:70px}
.card-text{margin-top:10px;font-size:15px;line-height:28.2px;color:#333;padding-right:6px}
.card-arrow{position:absolute;bottom:42px}
.partners-title{left:115px;top:732px;font-size:41px;font-family:'Merriweather',serif;font-weight:700}
.slider-arrows{left:1018px;top:760px;display:flex;gap:20px}
.logos{left:111px;top:841px;display:flex;gap:18px}
.logo-tile{width:181px;height:80px;background:var(--white);box-shadow:0 2px 6px rgba(0,0,0,.12);display:flex;align-items:center;justify-content:center}
.mark{width:40px;height:40px;background:#c9d3dc}

/* contact */
.contact{height:572px;background:var(--paper)}
.contact-title{left:0;width:1200px;text-align:center;top:90px;font-size:41px;font-family:'Merriweather',serif;font-weight:700}
.field{background:var(--white);box-shadow:0 2px 5px rgba(0,0,0,.06);font-size:14px;color:#555;padding:14px 24px}
.f-name{left:236px;top:177px;width:728px;height:45px}
.f-email{left:236px;top:241px;width:357px;height:45px}
.f-phone{left:607px;top:241px;width:357px;height:45px}
.f-msg{left:236px;top:313px;width:728px;height:118px}
.btn-submit{left:532px;top:462px;width:135px;height:42px;font-size:17px}

/* footer */
.site-footer{height:192px;background:var(--ink);color:var(--white)}
.footer-brand{left:130px;top:38px;font-family:'Merriweather',serif;color:var(--white);font-size:26px;line-height:31px}
.footer-nav{right:113px;top:66px;display:flex;gap:23px;font-size:17px}
.copyright{left:113px;top:142px;font-size:14.5px;color:#bbb}
.social{left:1017px;top:135px;display:flex;gap:14px}
.social span{width:29px;height:29px;border:1.5px solid var(--white);border-radius:50%}
</style>
</head>
<body>

<header class="site-header">
  <div class="abs brand">Kestrel<br>Capital Management</div>
  <nav class="abs main-nav"><a href="#">What we Do</a><a href="#">Our Team</a><a href="#">Investments</a><a href="#">Contact Us</a></nav>
  <a class="abs btn btn-start">Get Started</a>
  <h1 class="abs hero-title">Passion for uncovering<br>new opportunities</h1>
</header>

<section class="hero" role="img" aria-label="Aerial view of a container ship sailing across deep blue sea">
  <div class="abs btn btn-play">Play Video&nbsp;▶</div>
</section>

<section class="what">
  <h2 class="abs what-title">What we Do</h2>
  <p class="abs what-copy">A beacon of innovative investment where strategic diversification meets meticulous market comprehension. We navigate the complexities of Global Equities, Real Estate, Venture Capital, Private Equity, and Alternative Assets, focusing on uncovering distinctive investment opportunities for our investors.<br>At Kestrel, investment is not just a transaction; it's a carefully orchestrated process, mirroring the meticulous management of personal assets. Our ethos is built on a bedrock of expansive market wisdom and proactive strategy formulation, ensuring our portfolio remains both robust and agile.</p>
</section>

<section class="team">
  <h2 class="abs team-title">Our Team</h2>
  <h3 class="abs team-subtitle">The Architect of Kestrel's Visionary Path</h3>
  <p class="abs team-copy">Meet Marcus, the driving force behind Kestrel Capital Management. From co-founding Australia's second-largest renewable energy company to pioneering ventures in diverse sectors, Marcus's entrepreneurial journey is marked by a passion for market innovation and sustainable growth. With over a decade of diverse business scaling experience, Marcus established Kestrel Capital, evolving from personal investment to a trust-fortified endeavour of market innovation and niche investment exploration.</p>
  <div class="abs portrait" role="img" aria-label="Portrait photo of the fund founder in a navy suit"></div>
</section>

<section class="invest">
  <h2 class="abs invest-title">Investments</h2>
  <p class="abs invest-lead">Kestrel's portfolio showcases our ability to identify undervalued opportunities with significant growth potential.</p>
  <div class="abs cards">
    <article class="card"><h4 class="card-title">Venture Capital</h4><p class="card-text">Strategic investments in venture capital, where we harness our industry contacts and market understanding to invest in high growth startups and businesses.</p>
      <svg class="card-arrow" width="24" height="14" viewBox="0 0 24 14"><path d="M0 7H22M16 1L22 7L16 13" fill="none" stroke="#161616" stroke-width="1.4"/></svg></article>
    <article class="card"><h4 class="card-title">Private Equity</h4><p class="card-text">Access to investments in cutting edge sectors, featuring companies like Northwind AI, Chatterbox, Pixelwave, Datafold, Orbitex, Synapse, Freightline, Cortexa Systems and Arcade Games</p>
      <svg class="card-arrow" width="24" height="14" viewBox="0 0 24 14"><path d="M0 7H22M16 1L22 7L16 13" fill="none" stroke="#161616" stroke-width="1.4"/></svg></article>
    <article class="card"><h4 class="card-title">Global Equity Markets</h4><p class="card-text">We've demonstrated exceptional skill in identifying undervalued stocks and markets with high growth potential, leveraging in-depth research and market analysis</p>
      <svg class="card-arrow" width="24" height="14" viewBox="0 0 24 14"><path d="M0 7H22M16 1L22 7L16 13" fill="none" stroke="#161616" stroke-width="1.4"/></svg></article>
    <article class="card"><h4 class="card-title">Property Development</h4><p class="card-text">Curated development projects, exemplifying our ability to identify and capitalise on high-value real estate opportunities.</p>
      <svg class="card-arrow" width="24" height="14" viewBox="0 0 24 14"><path d="M0 7H22M16 1L22 7L16 13" fill="none" stroke="#161616" stroke-width="1.4"/></svg></article>
  </div>
  <h2 class="abs partners-title">Our Partners</h2>
  <div class="abs slider-arrows">
    <svg width="24" height="14" viewBox="0 0 24 14"><path d="M24 7H2M8 1L2 7L8 13" fill="none" stroke="#161616" stroke-width="1.4"/></svg>
    <svg width="24" height="14" viewBox="0 0 24 14"><path d="M0 7H22M16 1L22 7L16 13" fill="none" stroke="#161616" stroke-width="1.4"/></svg>
  </div>
  <div class="abs logos">
    <div class="logo-tile"><span class="mark"></span></div>
    <div class="logo-tile"><span class="mark"></span></div>
    <div class="logo-tile"><span class="mark"></span></div>
    <div class="logo-tile"><span class="mark"></span></div>
    <div class="logo-tile"><span class="mark"></span></div>
  </div>
</section>

<section class="contact">
  <h2 class="abs contact-title">Contact Us</h2>
  <div class="abs field f-name">Name</div>
  <div class="abs field f-email">Email</div>
  <div class="abs field f-phone">Phone</div>
  <div class="abs field f-msg">Message</div>
  <div class="abs btn btn-submit">Submit Now</div>
</section>

<footer class="site-footer">
  <div class="abs footer-brand">Kestrel<br>Capital Management</div>
  <nav class="abs footer-nav"><a href="#">What we Do</a><a href="#">Our Team</a><a href="#">Investments</a><a href="#">Contact Us</a></nav>
  <p class="abs copyright">2024 Kestrel Capital Management. All Rights Reserved.</p>
  <div class="abs social" aria-label="Social links"><span></span><span></span></div>
</footer>

</body>
</html>
```